Marta Quinlan Photography needs a unique, creative business card/logo design

I need a design for business cards/logo that is unique and creative in the industry. Simplicity is nice, so not too crowded. Something that will catch my customer's eye and remain in their memory. I am primarily a landscape photographer but will be soon may be branching into boudoir photography as well. I have attached my current card.

Industry/Entity Type

Business

Contact Information for Business Card

Marta Quinlan Photography
Phone: 0439 271 504
Email: MartaQuinlanPhotography@brivomail.net
Website: www.pagerly.net/MartaQuinlanPhotography.Aust

Logo Text

Marta Quinlan Photography

Requirements
Must have
• Contact Details on one side
Should not have
• pixelation

```html
<!DOCTYPE html>
<html lang="en">
<head>
<meta charset="utf-8">
<title>Marta Quinlan Photography — Business Card</title>
<link href="https://fonts.googleapis.com/css2?family=Roboto:wght@300;400;700&display=swap" rel="stylesheet">
<style>
  :root {
    --bg-light: #e4e4e4;
    --bg-dark: #c9c9c9;
    --card-black: #141414;
    --card-white: #f4f4f2;
    --silver: #b9b9b9;
    --text-light: #e6e6e6;
    --text-muted: #9a9a9a;
    --icon-bg: #f0f0f0;
  }
  * { box-sizing: border-box; margin: 0; padding: 0; }
  html, body { width: 1200px; height: 900px; overflow: hidden; }
  body {
    background: linear-gradient(135deg, var(--bg-light) 0%, var(--bg-dark) 100%);
    font-family: "Roboto", Arial, sans-serif;
    position: relative;
  }
  .card {
    position: absolute;
    width: 520px;
    height: 297px;
    box-shadow: 0 6px 18px rgba(0,0,0,0.18);
    overflow: hidden;
  }
  /* Front */
  .card--front {
    left: 100px; top: 110px;
    background: var(--card-black);
    display: flex; align-items: center; justify-content: center;
  }
  .brand-name {
    font-family: "Roboto", Arial, sans-serif;
    font-weight: 300;
    color: var(--silver);
    text-transform: uppercase;
    text-align: center;
    letter-spacing: 3px;
    line-height: 1.15;
  }
  .card--front .brand-name { font-size: 34px; }
  .card--front .brand-name small { display: block; font-size: 14px; letter-spacing: 6px; }

  /* Back */
  .card--back {
    left: 580px; top: 470px;
    background: var(--card-black);
  }
  .back-brand-panel {
    position: absolute; left: 0; top: 0;
    width: 215px; height: 100%;
    background: var(--card-white);
    display: flex; align-items: center; justify-content: center;
  }
  .back-brand-panel .brand-name { font-size: 22px; color: #a8a8a8; }
  .back-brand-panel .brand-name small { display: block; font-size: 9px; letter-spacing: 4px; }
  .tab {
    position: absolute;
    background: var(--card-black);
    width: 150px; height: 26px;
  }
  .tab--top { top: 0; left: 80px; }
  .tab--bottom { bottom: 0; left: 20px; }
  .corner-square {
    position: absolute; right: 0; top: 118px;
    width: 30px; height: 30px;
    background: var(--card-white);
  }
  .contact {
    position: absolute; left: 245px; top: 36px;
    color: var(--text-light);
  }
  .contact__name { font-weight: 700; font-size: 20px; }
  .contact__role { font-weight: 300; font-size: 12px; color: var(--text-muted); margin-top: 2px; }
  .contact__row {
    display: flex; align-items: center; gap: 14px;
    margin-top: 20px; font-size: 10px; font-weight: 300;
  }
  .contact__row:first-of-type { margin-top: 36px; }
  .icon {
    width: 24px; height: 24px; border-radius: 50%;
    background: var(--icon-bg);
    display: flex; align-items: center; justify-content: center;
    flex-shrink: 0;
  }
  .contact__web { margin-top: 22px; font-size: 10px; font-weight: 300; line-height: 1.35; }
</style>
</head>
<body>
  <section class="card card--front" aria-label="Business card front">
    <p class="brand-name">Marta Quinlan<small>Photography</small></p>
  </section>

  <section class="card card--back" aria-label="Business card back">
    <div class="back-brand-panel">
      <p class="brand-name">Marta Quinlan<small>Photography</small></p>
    </div>
    <div class="tab tab--top"></div>
    <div class="tab tab--bottom"></div>
    <div class="corner-square"></div>

    <div class="contact">
      <p class="contact__name">Marta Quinlan</p>
      <p class="contact__role">Photographer</p>

      <div class="contact__row">
        <span class="icon" aria-hidden="true">
          <svg width="12" height="12" viewBox="0 0 24 24"><path fill="#141414" d="M6.6 10.8c1.4 2.8 3.8 5.1 6.6 6.6l2.2-2.2c.3-.3.7-.4 1-.2 1.1.4 2.3.6 3.6.6.6 0 1 .4 1 1V20c0 .6-.4 1-1 1C10.6 21 3 13.4 3 4c0-.6.4-1 1-1h3.5c.6 0 1 .4 1 1 0 1.3.2 2.5.6 3.6.1.3 0 .7-.2 1z"/></svg>
        </span>
        <span>0439 271 504</span>
      </div>

      <div class="contact__row">
        <span class="icon" aria-hidden="true">
          <svg width="13" height="13" viewBox="0 0 24 24" fill="none" stroke="#141414" stroke-width="2"><circle cx="12" cy="12" r="9"/><ellipse cx="12" cy="12" rx="4" ry="9"/><line x1="3" y1="12" x2="21" y2="12"/><line x1="5" y1="7" x2="19" y2="7"/><line x1="5" y1="17" x2="19" y2="17"/></svg>
        </span>
      </div>

      <p class="contact__web">MartaQuinlanPhotography@brivomail.net<br>pagerly.net/MartaQuinlanPhotography.Aust</p>
    </div>
  </section>
</body>
</html>
```